We need a MODERN credit application banner

We have a program that helps people get pre-qualified for an auto loan. Our current Application page/Success page is dated and does not have the colors we want. I want to use fonts and colors that match our partner CrestLedger (www.crestledger.example). I want to include their powered by logo, pivot rating logo, and swift4lending logo all in a matching CrestLedger Color scheme. I also need a Favicon that matches your design for the page. I attached our deck so you can get more content. To be clear the application page and success pages below are the targets of this redesign! You can visit www.kbelmoreadvertising.example to get more information from our website or www.swift4lending.example.

Target Market(s)

Car dealers and their consumers

Industry/Entity Type

Automotive

Requirements
Must have
• It must offer the same data that is on the existing art
Nice to have
• Looking for a Clean but Interesting design.
Should not have
• No red and black. Do not change the form fills.

```html
<!DOCTYPE html>
<html lang="en">
<head>
<meta charset="utf-8">
<title>Swift4Lending Prequalification Banners</title>
<link href="https://fonts.googleapis.com/css2?family=Montserrat:wght@700;800;900&family=Roboto+Condensed:wght@400;700&family=Roboto:ital,wght@0,400;0,500;1,400&display=swap" rel="stylesheet">
<style>
:root{
  --bg:#a4a4a4;
  --teal:#1aa3c9;
  --teal-dark:#0e6f8a;
  --blue:#1f8fc5;
  --deep:#0d6e7c;
  --yellow:#f9d800;
  --orange:#ef7b1a;
  --ink:#222;
  --grey:#6a6a6a;
  --field-text:#444;
  --white:#fff;
}
*{box-sizing:border-box;margin:0;padding:0}
html,body{width:990px;height:1200px;overflow:hidden}
body{background:var(--bg);font-family:"Roboto",sans-serif;position:relative}
.card{position:absolute;left:88px;width:814px;background:var(--white);overflow:hidden;box-shadow:0 10px 30px rgba(0,0,0,.35)}
.application{top:75px;height:326px}
.success{top:427px;height:698px;background:linear-gradient(180deg,#f4f8fb 0%,#e7f1f8 60%,#f4f8fb 100%)}
.abs{position:absolute}
.powered{font-size:13px;color:#8a8a8a}
.brand-main{font-family:"Montserrat",sans-serif;font-weight:800;color:var(--teal);letter-spacing:-.5px}
.brand-small{font-family:"Roboto",sans-serif;font-weight:500;font-size:11px;color:#444;display:flex;align-items:center;gap:4px}
.brand-small .mark{width:9px;height:9px;background:var(--teal)}
.check{display:flex;align-items:center;gap:7px;font-family:"Roboto Condensed",sans-serif;font-size:10px;color:#222;text-transform:uppercase}
.check .box{width:8px;height:8px;border:1.2px solid #333}
.benefits{list-style:none;font-family:"Roboto Condensed",sans-serif;font-size:15px;color:#222}
.benefits li{display:flex;align-items:center;gap:9px;height:25px}
.btn{position:absolute;border-radius:30px;background:var(--yellow);color:var(--teal);font-family:"Montserrat",sans-serif;font-weight:800;display:flex;align-items:center;justify-content:center}
.bg-art{position:absolute;left:0;top:0}
.form{position:absolute;left:406px;top:30px;width:389px;display:grid;grid-template-columns:190px 190px;column-gap:9px;row-gap:7px}
.field{height:34px;background:var(--white);border-radius:2px;display:flex;align-items:center;justify-content:space-between;padding:0 14px 0 18px;font-size:11px;color:var(--field-text)}
.chev{width:7px;height:7px;border-right:1.4px solid #555;border-bottom:1.4px solid #555;transform:rotate(45deg) translateY(-2px)}
.vehicle-label{grid-column:1/3;font-family:"Roboto Condensed",sans-serif;font-weight:700;font-size:12.5px;color:var(--white);margin:2px 0 -1px}
.badge{position:absolute;left:271px;top:98px;width:176px;height:176px;border-radius:50%;background:var(--white);display:flex;align-items:center;justify-content:center}
.badge-inner{width:158px;height:158px;border-radius:50%;background:var(--orange);color:var(--white);font-family:"Roboto Condensed",sans-serif;font-weight:700;text-align:center;transform:rotate(-5deg);display:flex;flex-direction:column;justify-content:center;line-height:1.1}
.badge-inner .l1{font-size:16px}
.badge-inner .l2{font-size:20px;margin-top:4px}
.badge-inner .l3{font-family:"Montserrat",sans-serif;font-weight:900;font-size:29px;margin-top:2px}
.headline{font-family:"Roboto Condensed",sans-serif;font-weight:700;line-height:1}
.headline .a{font-size:27px;color:var(--teal-dark);display:block}
.headline .b{font-size:37px;color:var(--blue);display:block;margin-top:1px}
.steps{list-style:none;font-size:14.5px;color:var(--ink)}
.steps li{height:27.5px}
.steps a{color:var(--blue)}
.check.italic{font-style:italic;font-size:10.5px}
.validity{font-family:"Montserrat",sans-serif;font-weight:800;font-size:17.5px;color:var(--white);line-height:27px}
.act{position:absolute;left:50px;top:653px;width:198px;height:37px;background:var(--deep);color:var(--white);font-family:"Montserrat",sans-serif;font-weight:900;font-size:25px;display:flex;align-items:center;justify-content:center}
.score-title{font-family:"Roboto Condensed",sans-serif;font-weight:700;font-size:31px;color:var(--teal-dark);width:814px;left:0;text-align:center;padding-left:378px}
.score-line{font-family:"Montserrat",sans-serif;font-weight:900;font-size:21px;color:#1b1b1b}
.score-line span{color:var(--blue)}
.copy{left:434px;top:532px;width:345px;font-size:9.3px;line-height:16.3px;color:var(--grey);text-align:justify}
.copy u{text-decoration:underline}
</style>
</head>
<body>

<section class="card application">
  <svg class="bg-art" width="814" height="326" viewBox="0 0 814 326">
    <defs>
      <linearGradient id="formBg" x1="0" y1="0" x2="1" y2="1">
        <stop offset="0" stop-color="#0aa3cb"/>
        <stop offset="1" stop-color="#0a7daa"/>
      </linearGradient>
    </defs>
    <path d="M312,0 C372,90 372,220 209,326 L311,326 C420,200 420,80 382,0 Z" fill="var(--yellow)"/>
    <path d="M338,0 C385,90 385,200 300,300" stroke="#fff" stroke-width="8" fill="none"/>
    <path d="M382,0 C420,80 420,200 311,326 L814,326 L814,0 Z" fill="url(#formBg)" role="img" aria-label="Photo of a toy car on loan paperwork, tinted blue"/>
  </svg>

  <p class="abs powered" style="left:28px;top:15px">Powered by:</p>
  <p class="abs brand-main" style="left:28px;top:32px;font-size:30px">CrestLedger</p>
  <p class="abs brand-small" style="left:28px;top:95px">Swift4Lending</p>
  <p class="abs brand-small" style="left:116px;top:95px"><span class="mark"></span>PivotRating</p>

  <p class="abs check" style="left:26px;top:130px"><span class="box"></span>Check your buying power</p>
  <ul class="abs benefits" style="left:26px;top:156px">
    <li><svg width="15" height="12" viewBox="0 0 15 12"><path d="M1.5,6 L5.5,10 L13.5,1.5" stroke="var(--teal)" stroke-width="2.6" fill="none"/></svg>Free Credit Score</li>
    <li><svg width="15" height="12" viewBox="0 0 15 12"><path d="M1.5,6 L5.5,10 L13.5,1.5" stroke="var(--teal)" stroke-width="2.6" fill="none"/></svg>No Social Security number required</li>
    <li><svg width="15" height="12" viewBox="0 0 15 12"><path d="M1.5,6 L5.5,10 L13.5,1.5" stroke="var(--teal)" stroke-width="2.6" fill="none"/></svg>No Impact To Your Credit Score</li>
  </ul>
  <div class="btn" style="left:26px;top:255px;width:166px;height:47px;font-size:15px">GET RESULT</div>

  <form class="form">
    <div class="field">First Name *</div>
    <div class="field">Last Name *</div>
    <div class="field">Address *</div>
    <div class="field">Apartment *</div>
    <div class="field">City *</div>
    <div class="field">State *<span class="chev"></span></div>
    <div class="field">Zipcode *</div>
    <div class="field">Dtae of Birth *<span class="chev"></span></div>
    <div class="field">Mobile Phone *</div>
    <div class="field">Email Address *</div>
    <p class="vehicle-label">The Vehicle I'm interested in is :</p>
    <div class="field">Category *<span class="chev"></span></div>
    <div class="field">Make *<span class="chev"></span></div>
  </form>
</section>

<section class="card success">
  <svg class="bg-art" width="814" height="698" viewBox="0 0 814 698">
    <defs>
      <linearGradient id="heroBg" x1="0" y1="0" x2="1" y2="0">
        <stop offset="0" stop-color="#0e6f8a"/>
        <stop offset=".45" stop-color="#2d8fab"/>
        <stop offset=".7" stop-color="#c9dfea"/>
        <stop offset="1" stop-color="#eef4f8"/>
      </linearGradient>
    </defs>
    <rect x="0" y="0" width="814" height="246" fill="url(#heroBg)" role="img" aria-label="Photo of car keys on the left and hands sheltering a silver car on the right"/>
    <path d="M0,0 H650 C620,40 560,42 400,60 C250,78 100,82 0,60 Z" fill="#fff"/>
    <path d="M0,60 C100,82 250,78 400,60 C560,42 620,40 653,0 H675 C650,48 580,56 420,76 C260,96 100,102 0,95 Z" fill="var(--blue)"/>
    <path d="M0,698 V605 C90,540 200,522 290,536 C360,548 400,610 408,698 Z" fill="#d3e7f3"/>
    <path d="M0,698 V612 C90,550 200,532 282,546 C350,558 392,615 400,698 Z" fill="var(--blue)"/>
    <rect x="0" y="688" width="814" height="10" fill="var(--blue)"/>
  </svg>

  <p class="abs powered" style="left:63px;top:11px;font-size:9.5px">Powered by:</p>
  <p class="abs brand-main" style="left:63px;top:25px;font-size:22px">CrestLedger</p>
  <p class="abs brand-small" style="left:237px;top:27px;font-size:12px">Swift4Lending</p>
  <p class="abs brand-small" style="left:333px;top:28px"><span class="mark"></span>PivotRating</p>

  <div class="badge">
    <div class="badge-inner">
      <span class="l1">YOU PREQUALIFY</span>
      <span class="l2">FOR UP TO</span>
      <span class="l3">$75,000</span>
    </div>
  </div>

  <h1 class="abs headline" style="left:29px;top:266px"><span class="a">YOU CAN TAKE THE</span><span class="b">NEXT STEP</span></h1>
  <ol class="abs steps" style="left:29px;top:340px">
    <li>1.Call ABC Dealer at 303-555-0148</li>
    <li>2.Email them by <a href="#">Click here</a></li>
    <li>3.Print this page and take it to ABC Dealer</li>
  </ol>
  <p class="abs check italic" style="left:30px;top:430px"><span class="box"></span>Check your buying power</p>
  <div class="btn" style="left:29px;top:467px;width:232px;height:47px;font-size:12px">PRINT PREQUALIFICATION</div>

  <p class="abs validity" style="left:50px;top:585px">YOUR PREQUALIFICATION IS<br>VALID FOR A LIMITED TIME</p>
  <div class="act">ACT NOW!</div>

  <svg class="abs" style="left:456px;top:272px" width="280" height="152" viewBox="-140 -140 280 152">
    <path d="M-131,0 A131,131 0 0 1 131,0 L111,0 A111,111 0 0 0 -111,0 Z" fill="#e3e6e8"/>
    <g stroke="#fff" stroke-width="1.5">
      <path d="M-111,0 A111,111 0 0 1 -89.8,-65.3 L-32.4,-23.5 A40,40 0 0 0 -40,0 Z" fill="#d9261c"/>
      <path d="M-89.8,-65.3 A111,111 0 0 1 -34.3,-105.6 L-12.4,-38 A40,40 0 0 0 -32.4,-23.5 Z" fill="#ee6a0c"/>
      <path d="M-34.3,-105.6 A111,111 0 0 1 34.3,-105.6 L12.4,-38 A40,40 0 0 0 -12.4,-38 Z" fill="#f2b705"/>
      <path d="M34.3,-105.6 A111,111 0 0 1 89.8,-65.3 L32.4,-23.5 A40,40 0 0 0 12.4,-38 Z" fill="#b4cf0a"/>
      <path d="M89.8,-65.3 A111,111 0 0 1 111,0 L40,0 A40,40 0 0 0 32.4,-23.5 Z" fill="#63b32e"/>
    </g>
    <g font-family="Roboto Condensed, sans-serif" font-weight="700" font-size="16" fill="#8d9498" text-anchor="middle">
      <text x="0" y="-113">MEDIUM</text>
      <text transform="translate(-118,-30) rotate(-72)">LOW</text>
      <text transform="translate(118,-30) rotate(72)">HIGH</text>
    </g>
    <path d="M-4,-6 L74,-32 L76,-26 L4,6 Z" fill="#1f2a2e"/>
    <circle cx="0" cy="0" r="10" fill="#1f2a2e"/>
  </svg>

  <p class="abs score-title" style="top:437px">CREDIT SCORE</p>
  <p class="abs score-line" style="left:434px;top:492px">YOUR PIVOTRATING 3.0 <span>703</span></p>
  <p class="abs copy">Lorem <u>ipsum dolor sit amet</u>, consectetur adipiscing elit, sed do eiusmod tempor incididunt ut labore et dogna a ipsum suspendisse ultrices gravis comerra maecenas accumcus vel facilisis. Lorem ipsum dolor sit amesedipiscing elit, sed do eiusmod tempor incididunt ut labore et <u>dolore magna a ipsum suspendisse</u> ultrices gravis commodo viverra maecenas accumsan lacus vel facilisis. Lorem ipsum dolor sit amet,sectetur adipiscing elit do eiusmod tempor incididunt ut labore et dogna a ipsum suspendisse ultrices gravis commodo viverra maecenas accumcus vel facilisisrem <u>ipsuolor sit amesectetur</u> adipiscincididunt ut labore et dolore magna a ipsum suspendisse ultrices</p>
</section>

</body>
</html>
```